Diet product based by mushroom

My company name is HealtHomeIt means heal + home(healing & safe)Our target is women who are twenties - thirties having job & desire to lose weight within short terms about a week, two weeks, a monthMy company makes diet product based on mushrooms So we are looking for this packaging design of black mushroom + enoki mushroom. This product consists of one set(10 stick - each stick 3g) My company's main color is pastel yellow wish & white and company's mission is whoever we make relationship helps their life with mentally, physically We would like to see designs that use the color of our company logoThank you

Target Market(s)

Women who are twenties, thirties having job & desire to lose weight within short terms about a week, two weeks, a month

Colors
f6faec
eaf2ce
cadf82
abd036
9bcb3b

Requirements
Must have
• My project must have logo's color, the word (다온채, the food of gods')
• simple
Nice to have
• simple & highlight,legibility, simple&white
Should not have
• unbalance

```html
<!DOCTYPE html>
<html lang="ko">
<head>
<meta charset="utf-8">
<title>다온채 Package Front</title>
<link rel="stylesheet" href="https://fonts.googleapis.com/css2?family=Noto+Sans+KR:wght@300;400&family=Montserrat:wght@400&display=swap">
<style>
  :root {
    --backdrop: #e4e4e4;
    --panel-white: #ffffff;
    --brand-green: #5fb35a;
    --leaf-light: #cadf82;
    --leaf-mid: #abd036;
    --leaf-deep: #6cc41e;
    --ink: #3a3a3a;
    --tag-ink: #7a7a7a;
  }
  * { margin: 0; padding: 0; box-sizing: border-box; }
  html, body {
    width: 1200px;
    height: 884px;
    overflow: hidden;
    background: var(--backdrop);
  }
  .canvas {
    position: relative;
    width: 1200px;
    height: 884px;
  }
  .package-front {
    position: absolute;
    left: 435px;
    top: 192px;
    width: 330px;
    height: 500px;
    background: var(--panel-white);
    overflow: hidden;
  }
  .brand {
    position: absolute;
    top: 118px;
    left: 0;
    width: 100%;
    text-align: center;
  }
  .brand-mark {
    display: block;
    width: 14px;
    height: 14px;
    margin: 0 auto 10px;
    border-radius: 50%;
    background: var(--brand-green);
  }
  .brand-name {
    font-family: "Montserrat", sans-serif;
    font-weight: 400;
    font-size: 15px;
    letter-spacing: 2.5px;
    text-transform: uppercase;
    color: var(--brand-green);
  }
  .brand-tagline {
    margin-top: 3px;
    font-family: "Noto Sans KR", sans-serif;
    font-weight: 300;
    font-size: 7px;
    color: var(--tag-ink);
  }
  .product-name {
    position: absolute;
    top: 184px;
    left: 0;
    width: 100%;
    text-align: center;
    font-family: "Noto Sans KR", sans-serif;
    font-weight: 400;
    font-size: 40px;
    letter-spacing: 2px;
    color: var(--ink);
  }
  .green-field {
    position: absolute;
    left: 0;
    bottom: 0;
    width: 100%;
    height: 205px;
    background: linear-gradient(
      to bottom,
      rgba(255,255,255,1) 0%,
      var(--leaf-light) 22%,
      var(--leaf-mid) 55%,
      var(--leaf-deep) 100%
    );
  }
</style>
</head>
<body>
  <main class="canvas">
    <section class="package-front">
      <div class="brand">
        <span class="brand-mark"></span>
        <div class="brand-name">Zanterwik</div>
        <div class="brand-tagline">건강을 함께합니다. 힐링</div>
      </div>
      <h1 class="product-name">다온채</h1>
      <div class="green-field" role="img" aria-label="Soft green gradient with flowing wave lines and bokeh light dots"></div>
    </section>
  </main>
</body>
</html>
```